Business Card for Web Design consulting firm

Business card designs for Web Design consulting firm

Target Market(s)

English speaking adults ages 30 - 60. Predominantly professional services eg. Doctor, Dentist

Industry/Entity Type

Consulting

Requirements
Must have
• Double sided card

```html
<!DOCTYPE html>
<html lang="en">
<head>
<meta charset="utf-8">
<title>Korvela – Business Card, Front and Back</title>
<link rel="stylesheet" href="https://fonts.googleapis.com/css2?family=Alegreya:wght@400;700&display=swap">
<style>
  :root {
    --page-bg: #ffffff;
    --card-bg: #f2f2f2;
    --ink: #4d4d4d;
    --accent: #f7991f;
    --type: "Alegreya", serif;
  }
  html, body {
    margin: 0;
    padding: 0;
    width: 1200px;
    height: 881px;
    overflow: hidden;
    background: var(--page-bg);
    font-family: var(--type);
  }
  .sheet {
    position: relative;
    width: 1200px;
    height: 881px;
  }
  .card {
    position: absolute;
    top: 48px;
    width: 442px;
    height: 736px;
    background: var(--card-bg);
  }
  .card--front { left: 98px; }
  .card--back  { left: 590px; }

  .wordmark {
    position: absolute;
    display: flex;
    align-items: center;
    color: var(--ink);
    font-family: var(--type);
    font-weight: 400;
    white-space: nowrap;
  }
  .wordmark__dot {
    border-radius: 50%;
    background: var(--accent);
    flex: none;
  }
  .wordmark--large {
    left: 0;
    right: 0;
    top: 300px;
    justify-content: center;
    gap: 18px;
    font-size: 62px;
    letter-spacing: 6px;
  }
  .wordmark--large .wordmark__dot { width: 34px; height: 34px; }

  .wordmark--small {
    left: 71px;
    top: 84px;
    gap: 6px;
    font-size: 16px;
    letter-spacing: 1.5px;
  }
  .wordmark--small .wordmark__dot { width: 10px; height: 10px; }

  .contact {
    position: absolute;
    right: 71px;
    top: 506px;
    margin: 0;
    text-align: right;
    color: var(--ink);
    letter-spacing: 2.2px;
    font-size: 19px;
    line-height: 31px;
  }
  .contact__name {
    display: block;
    font-weight: 700;
    font-size: 20px;
    letter-spacing: 2.6px;
    line-height: 33px;
  }
  .contact__line { display: block; }
  .contact__label { margin-right: 6px; }
</style>
</head>
<body>
  <main class="sheet">
    <section class="card card--front" aria-label="Card front">
      <div class="wordmark wordmark--large">
        <span class="wordmark__dot"></span>
        <span class="wordmark__name">KORVELA</span>
      </div>
    </section>

    <section class="card card--back" aria-label="Card back">
      <div class="wordmark wordmark--small">
        <span class="wordmark__dot"></span>
        <span class="wordmark__name">KORVELA</span>
      </div>
      <address class="contact" style="font-style: normal;">
        <span class="contact__name">Your Name</span>
        <span class="contact__line"><span class="contact__label">p</span>(555) 555-5555</span>
        <span class="contact__line"><span class="contact__label">f</span>(555) 555-5555</span>
        <span class="contact__line">yourname@korvela.com</span>
        <span class="contact__line">www.website.com</span>
      </address>
    </section>
  </main>
</body>
</html>
```